Business Card Design Project

In addition to the logo design we want a professional and contemporary business card for a talent management agency. We provide management services to creative artists and want to communicate a professional creative vibe.
Updates

Project Deadline Extended
Reason: Sorry didnt realise I had put such a short timeline on it.

Target Market(s)

The business deals with creative artists and other industry professionals

Industry/Entity Type

Artists

Colors

Designer to choose colors to be used in the design.

Requirements
Must have
• Logo
Address
Phone
Email

```html
<!DOCTYPE html>
<html lang="en">
<head>
<meta charset="utf-8">
<title>Velora Artists – Business Card</title>
<link href="https://fonts.googleapis.com/css2?family=Arimo:wght@400;700&display=swap" rel="stylesheet">
<style>
  :root {
    --backdrop: #3b322d;
    --card-black: #1e1e1e;
    --card-white: #ffffff;
    --ink: #222222;
    --ink-soft: #6f6f6f;
    --on-dark: #f2f2f2;
    --on-dark-soft: #b9b9b9;
    --band-dark: #2f2f2f;
    --band-mid: #555555;
    --faint-mark: rgba(255,255,255,0.07);
  }
  * { box-sizing: border-box; margin: 0; padding: 0; }
  html, body {
    width: 1200px; height: 741px; overflow: hidden;
    background: var(--backdrop);
    font-family: "Arimo", Arial, sans-serif;
  }
  .stage {
    position: relative; width: 1200px; height: 741px;
    display: flex; align-items: center; justify-content: center; gap: 40px;
  }
  .card {
    position: relative; width: 520px; height: 297px;
    border-radius: 4px; overflow: hidden;
    box-shadow: 0 10px 28px rgba(0,0,0,0.45);
  }

  /* Front */
  .card--front { background: var(--card-black); }
  .front__mark {
    position: absolute; left: 40px; top: 18px;
    width: 110px; height: 110px; border-radius: 50%;
    border: 6px solid var(--faint-mark);
  }
  .front__brand {
    position: absolute; right: 34px; bottom: 42px; text-align: left;
  }
  .brand {
    display: flex; align-items: center; gap: 10px;
  }
  .brand__dot {
    width: 38px; height: 38px; border-radius: 50%;
    border: 3px solid currentColor;
  }
  .brand__name { font-weight: 700; font-size: 27px; letter-spacing: 0.2px; }
  .front__brand .brand { color: var(--on-dark); }
  .front__web {
    margin-top: 8px; color: var(--on-dark-soft);
    font-size: 15px; letter-spacing: 4px;
  }

  /* Back */
  .card--back { background: var(--card-white); color: var(--ink); }
  .back__brand { position: absolute; top: 34px; left: 0; right: 0; display: flex; justify-content: center; }
  .back__brand .brand { color: var(--ink); }
  .person { position: absolute; top: 112px; left: 0; right: 0; text-align: center; }
  .person__name { font-size: 21px; font-weight: 700; letter-spacing: 0.5px; }
  .person__role { font-size: 12px; color: var(--ink-soft); margin-top: 2px; }

  .contacts {
    position: absolute; top: 170px; left: 0; right: 0;
    display: flex; justify-content: center; gap: 46px; font-size: 12.5px;
  }
  .contacts__col { display: flex; flex-direction: column; gap: 8px; }
  .contacts__col--left { align-items: flex-end; }
  .contact { display: flex; align-items: center; gap: 8px; }
  .contact svg { width: 12px; height: 12px; fill: var(--ink); flex: none; }

  .band {
    position: absolute; left: 0; right: 0; bottom: 0; height: 32px;
    background: linear-gradient(180deg, #666 0%, var(--band-mid) 100%);
  }
  .band__block {
    position: absolute; left: 0; bottom: 0; width: 196px; height: 58px;
    background: var(--band-dark);
    border-right: 4px solid var(--card-white);
  }
</style>
</head>
<body>
<main class="stage">
  <section class="card card--front" aria-label="Card front">
    <div class="front__mark" aria-hidden="true"></div>
    <div class="front__brand">
      <div class="brand">
        <span class="brand__dot" aria-hidden="true"></span>
        <span class="brand__name">Velora Artists</span>
      </div>
      <div class="front__web">www.website.com</div>
    </div>
  </section>

  <section class="card card--back" aria-label="Card back">
    <div class="back__brand">
      <div class="brand">
        <span class="brand__dot" aria-hidden="true"></span>
        <span class="brand__name">Velora Artists</span>
      </div>
    </div>

    <div class="person">
      <div class="person__name">JORDAN VALE</div>
      <div class="person__role">Developer</div>
    </div>

    <div class="contacts">
      <div class="contacts__col contacts__col--left">
        <div class="contact">Type your location here
          <svg viewBox="0 0 24 24" aria-hidden="true"><path d="M12 2a7 7 0 0 0-7 7c0 5 7 13 7 13s7-8 7-13a7 7 0 0 0-7-7zm0 9.5A2.5 2.5 0 1 1 12 6.5a2.5 2.5 0 0 1 0 5z"/></svg>
        </div>
        <div class="contact">your@mailbox.com
          <svg viewBox="0 0 24 24" aria-hidden="true"><path d="M2 5h20v14H2z M3.5 6.5 12 13l8.5-6.5" /></svg>
        </div>
      </div>
      <div class="contacts__col">
        <div class="contact">
          <svg viewBox="0 0 24 24" aria-hidden="true"><path d="M6.6 10.8a15 15 0 0 0 6.6 6.6l2.2-2.2a1 1 0 0 1 1-.25 11.4 11.4 0 0 0 3.6.57 1 1 0 0 1 1 1V20a1 1 0 0 1-1 1A17 17 0 0 1 3 4a1 1 0 0 1 1-1h3.5a1 1 0 0 1 1 1c0 1.25.2 2.45.57 3.6a1 1 0 0 1-.25 1z"/></svg>
          (+84)0900123456
        </div>
        <div class="contact">
          <svg viewBox="0 0 24 24" aria-hidden="true"><path d="M12 2a10 10 0 1 0 0 20 10 10 0 0 0 0-20zm6.9 6h-2.9a15 15 0 0 0-1.4-3.6A8 8 0 0 1 18.9 8zM12 4c.8 1.2 1.5 2.5 1.9 4h-3.8c.4-1.5 1.1-2.8 1.9-4zM4.3 14a8 8 0 0 1 0-4h3.4a16 16 0 0 0 0 4zm.8 2h2.9c.3 1.3.8 2.5 1.4 3.6A8 8 0 0 1 5.1 16zM8 8H5.1a8 8 0 0 1 4.3-3.6C8.8 5.5 8.3 6.7 8 8zm4 12c-.8-1.2-1.5-2.5-1.9-4h3.8c-.4 1.5-1.1 2.8-1.9 4zm2.3-6H9.7a14 14 0 0 1 0-4h4.6a14 14 0 0 1 0 4zm.3 5.6c.6-1.1 1.1-2.3 1.4-3.6h2.9a8 8 0 0 1-4.3 3.6zm1.7-5.6a16 16 0 0 0 0-4h3.4a8 8 0 0 1 0 4z"/></svg>
          www.website.com
        </div>
      </div>
    </div>

    <div class="band" aria-hidden="true"></div>
    <div class="band__block" aria-hidden="true"></div>
  </section>
</main>
</body>
</html>
```